Reel-Rot Carnival Podcast Cover Design

We need a podcast cover (square design) for a podcast called Reel-Rot Carnival.
MANDATORY: REEL-ROT CARNIVAL
OPTIONAL: with The Creepshow Nerd Dale Ostrund

Reel-Rot Carnival is a movie podcast dedicated to covering all of the cult oddities you saw in theaters and video stores as a kid but never got to rent or watch. Focusing on obscure horror, cult oddities, action movies, exploitation movies, foreign knockoffs, and more, this a show designed to help you take a trip down memory lane or find new weird movies to add to your streaming queue. Come take a walk on the wild side of cinema at Reel-Rot Carnival,..where one person's trash movie is our treasure.
##
Fonts that fit the vibe we're going for:
https://www.glyphcrate.example/sets/gore-drip-type-lettervolk
https://www.pinboardly.example/pin/871204563390157224/
https://www.glyphcrate.example/sets/gore-vintage-type-lettervolk

Target Market(s)

Primarily male, although we have some female fans as well. Podcast fans of B-movies (inexpensively made and a bit outrageous), cult movies, weird movies, old movies, horror movies, and action films.

Industry/Entity Type

Media - Movies -Podcast

Font styles to use
Other font styles liked:
• Fonts that fit the vibe: Fonts: https://www.glyphcrate.example/sets/gore-drip-type-lettervolk https://www.pinboardly.example/pin/871204563390157224/ https://www.glyphcrate.example/sets/gore-vintage-type-lettervolk

Colors
EB3D1F
EC4F4E
F09395
F8D3D4
FCEDEE

Requirements
Must have
• REEL-ROT CARNIVAL
Nice to have
• 1) with The Creepshow Nerd Dale Ostrund; 2) VISUALS: VHS tapes

```html
<!DOCTYPE html>
<html lang="en">
<head>
<meta charset="utf-8">
<title>Reel-Rot Carnival — Podcast Cover</title>
<link rel="stylesheet" href="https://fonts.googleapis.com/css2?family=Bangers&family=Creepster&family=Poppins:wght@500&display=swap">
<style>
  :root {
    --blood-red: #ff0a0a;
    --bone-white: #ffffff;
    --night-teal: #1f3a42;
    --deep-teal: #0c1a1f;
    --mist-teal: #3f6f7a;
    --strip-frame: #7fb3bf;
    --strip-cell: #05090b;
  }
  * { margin: 0; padding: 0; box-sizing: border-box; }
  html, body {
    width: 1200px;
    height: 1200px;
    overflow: hidden;
    background: var(--deep-teal);
  }
  .cover {
    position: relative;
    width: 1200px;
    height: 1200px;
    overflow: hidden;
  }
  .cover-backdrop {
    position: absolute;
    inset: 0;
    background:
      radial-gradient(ellipse 60% 45% at 55% 48%, var(--mist-teal) 0%, transparent 70%),
      radial-gradient(ellipse 90% 80% at 50% 40%, var(--night-teal) 0%, var(--deep-teal) 100%);
  }
  .film-strip {
    position: absolute;
    left: 0;
    top: 626px;
    width: 1200px;
    height: 300px;
    background: linear-gradient(180deg,
      transparent 0%,
      var(--strip-frame) 4%,
      var(--strip-frame) 15%,
      var(--strip-cell) 17%,
      var(--strip-cell) 83%,
      var(--strip-frame) 85%,
      var(--strip-frame) 96%,
      transparent 100%);
    opacity: 0.75;
  }
  .title {
    position: absolute;
    left: 0;
    top: 0;
    width: 1200px;
    height: 640px;
  }
  .title-line {
    font-family: 'Bangers', cursive;
  }
  .title-line--red { font-size: 400px; fill: var(--blood-red); }
  .title-line--white { font-size: 320px; fill: var(--bone-white); }
  .host {
    position: absolute;
    left: 0;
    width: 1200px;
    text-align: center;
  }
  .host-tagline {
    top: 962px;
    font-family: 'Poppins', sans-serif;
    font-weight: 500;
    font-size: 30px;
    letter-spacing: 4px;
    color: var(--bone-white);
    text-transform: uppercase;
    line-height: 1.2;
  }
  .host-name {
    top: 1016px;
    font-family: 'Creepster', cursive;
    font-size: 108px;
    letter-spacing: 10px;
    color: var(--blood-red);
    text-transform: uppercase;
    line-height: 1;
  }
</style>
</head>
<body>
  <main class="cover">
    <div class="cover-backdrop" role="img" aria-label="Dark teal grunge wall texture with faint drips"></div>
    <div class="film-strip" role="img" aria-label="Curving strip of cinema film running across the cover"></div>

    <svg class="title" viewBox="0 0 1200 640" aria-label="Reel-Rot Carnival">
      <text class="title-line title-line--red" x="80" y="378" textLength="1010" lengthAdjust="spacingAndGlyphs">REEL-ROT</text>
      <text class="title-line title-line--white" x="95" y="612" textLength="990" lengthAdjust="spacingAndGlyphs">CARNIVAL</text>
    </svg>

    <p class="host host-tagline">With The Fright-Flick Nerd</p>
    <p class="host host-name">Dale Ostrund</p>
  </main>
</body>
</html>
```